One page website

I'm looking for a landing page for my company. Just a brief description of our medical device technology with some images

Coding

Coded - Design and coding required

```html
<!DOCTYPE html>
<html lang="en">
<head>
<meta charset="UTF-8">
<title>Landing Page</title>
<link href="https://fonts.googleapis.com/css2?family=Raleway:wght@400;500;600;700;800&display=swap" rel="stylesheet">
<style>
  :root {
    --brand-blue: #38a3dc;
    --brand-green: #9bc93b;
    --ink: #000000;
    --white: #ffffff;
    --section-tint: #e0e8ee;
    --photo-dark: #4a4a4a;
    --photo-light: #d9d9d9;
  }
  * { margin: 0; padding: 0; box-sizing: border-box; }
  html, body { width: 869px; height: 1200px; overflow: hidden; }
  body {
    position: relative;
    font-family: 'Raleway', sans-serif;
    background: var(--white);
    color: var(--ink);
  }
  .site-header {
    position: absolute; left: 0; top: 0; width: 869px; height: 55px;
    background: var(--white);
  }
  .logo {
    position: absolute; left: 66px; top: 15px;
    font-size: 20px; font-weight: 800; color: var(--brand-blue);
  }
  .main-nav a {
    position: absolute; top: 22px;
    font-size: 13px; font-weight: 600; color: var(--brand-blue);
    text-decoration: none; letter-spacing: 0.2px;
  }
  .nav-cta {
    position: absolute; left: 737px; top: 17px; width: 87px; height: 26px;
    border-radius: 13px; background: var(--brand-blue);
  }
  .hero {
    position: absolute; left: 0; top: 55px; width: 869px; height: 429px;
    background: linear-gradient(105deg, var(--brand-blue) 0%, #6dba80 50%, var(--brand-green) 100%);
    overflow: hidden;
  }
  .hero-photo {
    position: absolute; left: 425px; top: 40px; width: 400px; height: 389px;
    border-radius: 160px 160px 0 0;
    background: radial-gradient(ellipse at 50% 45%, #cfcfcf 0%, #8a8a8a 60%, rgba(90,90,90,0.6) 100%);
    opacity: 0.85;
  }
  .hero-title {
    position: absolute; left: 64px; top: 82px;
    font-size: 59px; font-weight: 600; line-height: 48px; color: var(--white);
    letter-spacing: -0.5px;
  }
  .hero-lead {
    position: absolute; left: 66px; top: 250px;
    font-size: 18px; font-weight: 500; line-height: 22px; color: var(--white);
  }
  .hero-cta {
    position: absolute; left: 66px; top: 260px; width: 127px; height: 34px;
    margin-top: 55px;
    border-radius: 17px; background: var(--white);
  }
  .section-title {
    position: absolute; left: 0; width: 869px; text-align: center;
    font-size: 29px; font-weight: 800; letter-spacing: 0.3px;
  }
  .mission-title { top: 492px; }
  .mission-photo {
    position: absolute; left: 75px; top: 569px; width: 283px; height: 189px;
    border-radius: 10px;
    background: radial-gradient(ellipse at 65% 60%, #f2f2f2 0%, #9a9a9a 45%, var(--photo-dark) 100%);
    box-shadow: 0 3px 10px rgba(0,0,0,0.12);
  }
  .mission-copy { position: absolute; left: 390px; top: 563px; }
  .mission-copy h3 { font-size: 24px; font-weight: 700; line-height: 30px; }
  .mission-copy .kicker { font-size: 18px; font-weight: 500; color: var(--brand-blue); line-height: 24px; }
  .mission-copy p { margin-top: 13px; font-size: 18px; font-weight: 500; line-height: 22px; }
  .problem {
    position: absolute; left: 0; top: 803px; width: 869px; height: 397px;
    background: var(--section-tint);
  }
  .problem-title { top: 12px; }
  .problem-card {
    position: absolute; top: 72px; width: 236px; height: 330px;
    background: var(--white); border-radius: 9px 9px 0 0; overflow: hidden;
    text-align: center;
  }
  .card-photo {
    height: 158px; border-bottom: 5px solid var(--brand-blue);
    background: radial-gradient(ellipse at 65% 60%, #f2f2f2 0%, #9a9a9a 45%, var(--photo-dark) 100%);
  }
  .problem-card h4 { margin-top: 11px; font-size: 14.5px; font-weight: 700; }
  .problem-card p {
    margin: 8px auto 0; width: 170px;
    font-size: 10.8px; font-weight: 500; line-height: 13px;
  }
</style>
</head>
<body>
  <header class="site-header">
    <div class="logo">LOGO</div>
    <nav class="main-nav">
      <a href="#mission" style="left:378px">MISSION</a>
      <a href="#problem" style="left:459px">PROBLEM</a>
      <a href="#solution" style="left:547px">SOLUTION</a>
      <a href="#founders" style="left:640px">FOUNDERS</a>
    </nav>
    <div class="nav-cta"></div>
  </header>

  <section class="hero">
    <div class="hero-photo" role="img" aria-label="Back view of a man holding his neck and lower back, spine highlighted in blue with red pain areas"></div>
    <h1 class="hero-title">Lorem ipsum<br>dolor sitametan</h1>
    <p class="hero-lead">Lorem ipsum dolor sit amet, consectetur<br>adipiscing elit, sed do eiusmod tempor</p>
    <div class="hero-cta"></div>
  </section>

  <h2 class="section-title mission-title" id="mission">MISSION</h2>
  <div class="mission-photo" role="img" aria-label="Man with back pain, spine highlighted"></div>
  <div class="mission-copy">
    <h3>Lorem ipsum dolor sit amet</h3>
    <div class="kicker">Lorem ipsum</div>
    <p>Lorem ipsum dolor sit amet, consectetur<br>adipiscing elit, sed do eiusmod tempor</p>
  </div>

  <section class="problem" id="problem">
    <h2 class="section-title problem-title">PROBLEM</h2>
    <article class="problem-card" style="left:68px">
      <div class="card-photo" role="img" aria-label="Man with back pain, spine highlighted"></div>
      <h4>Lorem ipsum dolor sit amet,</h4>
      <p>Lorem ipsum dolor sit amet, consectetur adipiscing elit, sed do eiusmod tempor incididunt ut labore et dolore magna aliqua. Quis ipsum sus­pendisse ultrices gravida. Risus commodo viverra maecenas.</p>
    </article>
    <article class="problem-card" style="left:316px">
      <div class="card-photo" role="img" aria-label="Man with back pain, spine highlighted"></div>
      <h4>Lorem ipsum dolor sit amet,</h4>
      <p>Lorem ipsum dolor sit amet, consectetur adipiscing elit, sed do eiusmod tempor incididunt ut labore et dolore magna aliqua. Quis ipsum sus­pendisse ultrices gravida. Risus commodo viverra maecenas.</p>
    </article>
    <article class="problem-card" style="left:565px">
      <div class="card-photo" role="img" aria-label="Man with back pain, spine highlighted"></div>
      <h4>Lorem ipsum dolor sit amet,</h4>
      <p>Lorem ipsum dolor sit amet, consectetur adipiscing elit, sed do eiusmod tempor incididunt ut labore et dolore magna aliqua. Quis ipsum sus­pendisse ultrices gravida. Risus commodo viverra maecenas.</p>
    </article>
  </section>
</body>
</html>
```